Brochure design

I have attached our current prospectus which has been created by ourselves, we are looking for this now to be professionally designed. We are happy to use the content but also for this to be amended to co-incide with the message on our website www.thistlewick.co.uk and for it to be condensed into a more reader friendly format. Whilst we are happy with this website, again it was created by ourselves and we are not necessarily following the same design features but the colour scheme should be similar to the website. The prospectus will be printed on 2 x A4 sheets folded to make an 8 page A5 booklet with page 1 being a front cover and page 8 being back cover with contact information. The business is a childrens day nursery so the prospectus should be bright, fun, to the point and informative. I am happy to provide any further information to designers who may be looking at this by emailing me dana@thistlewick.co.uk . The completed product should allow us to edit the text for example to communicate price changes.

Further information:

Thistlewick Nursery is very unique compared with other Nurseries. Most nurseries segregate age groups into different rooms whereas at Thistlewick aged groups mix together to create a homely environment and also children are not moving through different rooms every year. Could we therefore get a message through the prospectus which reflects this, we currently use a strapline "A unique home from home childcare experience" but we are looking to change this and will be grateful for ideas.

We have no preference whether stock images are used or our own, However, stock images and ours should not be included on the same page.

From the designs received we do like stock images for the front and back cover but these must be relevant, ie showing children aged 3 months old to 5 years old.

Target Market(s)

Mum's mainly but Dad's also of children aged 0 to 5 years old. Age range of parents between 22 and 45.

Industry/Entity Type

Environment

Font styles to use
Serif

Colors
acd036
b768aa
e9f1ce
ecdaeb
ceeae6

Requirements
Must have
• Fun, Colorfull, Bright, Concise, Informative.
Should not have
• Stock images and supplied images on the same pages

```html
<!DOCTYPE html>
<html lang="en">
<head>
<meta charset="utf-8">
<title>Thistlewick Nursery – Prospectus pages 6–7</title>
<link rel="stylesheet" href="https://fonts.googleapis.com/css2?family=Lora:ital,wght@0,400;0,700;1,700&display=swap">
<style>
  :root {
    --backdrop: #c9c9c9;
    --paper: #fbfcf6;
    --paper-fold: #e4e8d6;
    --lime: #acd036;
    --lime-deep: #5f7a12;
    --plum: #b768aa;
    --plum-deep: #8e3f82;
    --mint: #ceeae6;
    --pale-lime: #e9f1ce;
    --pale-plum: #ecdaeb;
  }
  * { box-sizing: border-box; margin: 0; padding: 0; }
  html, body {
    width: 1200px; height: 791px; overflow: hidden;
    background: var(--backdrop);
    font-family: "Lora", serif;
  }
  .spread {
    position: absolute; left: 105px; top: 45px;
    width: 990px; height: 700px;
    display: flex;
    box-shadow: 0 12px 30px rgba(0,0,0,.25);
  }
  .page { position: relative; width: 495px; height: 700px; }
  .page--left { background: linear-gradient(270deg, var(--paper-fold) 0, var(--paper) 28px); }
  .page--right { background: linear-gradient(90deg, var(--paper-fold) 0, var(--paper) 28px); }
  .page-title {
    position: absolute; top: 92px; left: 0; right: 0;
    text-align: center;
    font-style: italic; font-weight: 700;
    font-size: 36px; line-height: 1.25;
    color: var(--plum);
  }
  .hero-photo {
    position: absolute; left: 62px; top: 200px;
    width: 330px; height: 260px;
    background:
      radial-gradient(ellipse at 78% 42%, #f3b45a 0, transparent 36%),
      radial-gradient(ellipse at 76% 82%, #5a8fd0 0, transparent 28%),
      radial-gradient(ellipse at 18% 62%, #f2a7cd 0, transparent 32%),
      radial-gradient(ellipse at 46% 62%, #a9c7de 0, transparent 32%),
      var(--paper);
  }
  .contact {
    position: absolute; top: 478px; left: 20px; right: 20px;
    text-align: center; font-style: normal;
    color: var(--plum-deep);
    font-size: 15px; line-height: 1.4;
  }
  .contact strong { font-weight: 700; }
  .folio {
    position: absolute; bottom: 28px;
    display: flex; align-items: center; gap: 8px;
  }
  .folio--left { left: 32px; }
  .folio--right { right: 32px; }
  .folio__number {
    width: 26px; height: 22px;
    background: var(--lime); color: #fff;
    font-size: 12px; font-weight: 700;
    display: flex; align-items: center; justify-content: center;
  }
  .folio__name { font-size: 15px; font-weight: 700; color: var(--plum); }
  .body-copy {
    position: absolute; left: 62px; width: 375px; top: 88px;
    color: var(--lime-deep);
    font-size: 15.5px; line-height: 1.32;
  }
  .body-copy p { margin-bottom: 20px; }
  .body-copy .aside { padding-left: 44px; color: var(--plum-deep); font-weight: 700; }
</style>
</head>
<body>
  <main class="spread">
    <section class="page page--left">
      <h1 class="page-title">So what do you<br>do next?</h1>
      <div class="hero-photo" role="img" aria-label="Photo of four toddlers kneeling together, one boy in an orange top waving"></div>
      <address class="contact">
        <strong>Contact us at,</strong><br>
        12 Fernwood Close, Ashbury<br>
        AB4 7QT<br>
        Phone: <strong>01632960482</strong><br>
        Email: <strong>enquiries@thistlewick.co.uk</strong>
      </address>
      <footer class="folio folio--left">
        <span class="folio__number">6</span>
        <span class="folio__name">Thistlewick</span>
      </footer>
    </section>

    <section class="page page--right">
      <div class="body-copy">
        <p>If you have decided that Thistlewick Day Nursery is right for your child and yourself, then the next step is to register with us...</p>
        <p>You can rest assured that you will be welcomed into our nursery at a pace which suits you and your families’ needs.</p>
        <p>Start by returning the registration form to us, along with some dates of which you can visit the nursery to begin the settling in process and complete the necessary forms that we need.</p>
        <p class="aside">It really is that easy!</p>
        <p>However, if you feel that a nursery environment isn’t what your family needs right now, don’t worry, please ask us about other childcare settings and we will be happy to recommend somewhere which will match your needs and we thank you for enquiring with us.</p>
      </div>
      <footer class="folio folio--right">
        <span class="folio__name">Thistlewick</span>
        <span class="folio__number">7</span>
      </footer>
    </section>
  </main>
</body>
</html>
```